Company director needs a business card design

I am a semi-retired former senior finance executive who sits on a number of public and private company boards and do some consulting work. I work largely with emerging businesses but deal regularly with top end of town lawyers, bankers etc. I need a thoughtful but relatively conservative design which would also resonate with my younger client base. Some colour would be good. Information limited to name, address, office tel, mobile and email.

Industry/Entity Type

Finance

```html
<!DOCTYPE html>
<html lang="en">
<head>
<meta charset="utf-8">
<title>Malcolm Ashford – Business Card</title>
<link rel="stylesheet" href="https://fonts.googleapis.com/css2?family=Gelasio:wght@400;700&display=swap">
<style>
  :root {
    --paper: #ffffff;
    --ink: #111111;
    --royal: #0a4ea6;
    --ornament: #2f64a6;
    --ornament-soft: #6f95c8;
    --back-ornament: #ffffff;
  }
  * { box-sizing: border-box; margin: 0; padding: 0; }
  html, body {
    width: 1036px;
    height: 1200px;
    overflow: hidden;
    background: var(--paper);
  }
  body {
    font-family: "Gelasio", Georgia, serif;
    color: var(--ink);
  }
  .card-set { position: relative; width: 1036px; height: 1200px; }

  /* Front side */
  .card-front {
    position: absolute; left: 0; top: 0;
    width: 1036px; height: 601px;
    background: var(--paper);
  }
  .holder-name {
    position: absolute; left: 0; top: 122px; width: 100%;
    text-align: center;
    font-size: 72px; font-weight: 400; line-height: 1;
  }
  .flourish {
    position: absolute;
    border-radius: 40px;
  }
  .flourish--left  { left: 115px; top: 142px; width: 128px; height: 80px;
    background: linear-gradient(90deg, var(--ornament), var(--ornament-soft)); }
  .flourish--right { left: 832px; top: 142px; width: 128px; height: 80px;
    background: linear-gradient(270deg, var(--ornament), var(--ornament-soft)); }
  .flourish--under { left: 232px; top: 206px; width: 588px; height: 48px;
    background: linear-gradient(90deg, var(--ornament-soft), var(--ornament), var(--ornament-soft)); }

  .contact-row {
    position: absolute; left: 120px; right: 110px; top: 290px;
    display: flex; justify-content: space-between;
    font-size: 36px; line-height: 1;
  }
  .contact-line {
    position: absolute; left: 0; width: 100%;
    text-align: center; font-size: 36px; line-height: 1;
  }
  .contact-line--email   { top: 364px; }
  .contact-line--address { top: 458px; }

  /* Back side */
  .card-back {
    position: absolute; left: 0; top: 601px;
    width: 1036px; height: 599px;
    background: var(--royal);
  }
  .corner-piece {
    position: absolute; width: 84px; height: 90px;
    background: var(--back-ornament); opacity: 0.85;
    border-radius: 10px;
  }
  .corner-piece--tl { left: 31px;  top: 128px; }
  .corner-piece--tr { left: 920px; top: 128px; }
  .corner-piece--bl { left: 31px;  top: 372px; }
  .corner-piece--br { left: 920px; top: 372px; }
  .back-flourish {
    position: absolute; left: 154px; top: 305px; width: 729px; height: 60px;
    border-radius: 30px;
    background: linear-gradient(90deg, rgba(255,255,255,0.04), rgba(255,255,255,0.16), rgba(255,255,255,0.04));
  }
  .back-email {
    position: absolute; left: 0; top: 278px; width: 100%;
    text-align: center; color: var(--paper);
    font-size: 34px; font-weight: 700; line-height: 1;
  }
</style>
</head>
<body>
<main class="card-set">
  <section class="card-front">
    <div class="flourish flourish--left" role="img" aria-label="Decorative blue scroll ornament"></div>
    <h1 class="holder-name">Malcolm Ashford</h1>
    <div class="flourish flourish--right" role="img" aria-label="Decorative blue scroll ornament"></div>
    <div class="flourish flourish--under" role="img" aria-label="Decorative blue flourish beneath the name"></div>

    <div class="contact-row">
      <span class="contact-tel">Tel: 02 9841 5260</span>
      <span class="contact-mobile">Mobile: 0412 583 207</span>
    </div>
    <p class="contact-line contact-line--email">Email: Malcolm_Ashford@tidemail.net.au</p>
    <p class="contact-line contact-line--address">Address: 18 Wattle Crescent, Seaview NSW 2099</p>
  </section>

  <section class="card-back">
    <div class="corner-piece corner-piece--tl" role="img" aria-label="White corner fleuron ornament"></div>
    <div class="corner-piece corner-piece--tr" role="img" aria-label="White corner fleuron ornament"></div>
    <div class="back-flourish" role="img" aria-label="Faint decorative flourish"></div>
    <p class="back-email">Malcolm_Ashford@tidemail.net.au</p>
    <div class="corner-piece corner-piece--bl" role="img" aria-label="White corner fleuron ornament"></div>
    <div class="corner-piece corner-piece--br" role="img" aria-label="White corner fleuron ornament"></div>
  </section>
</main>
</body>
</html>
```